Need help in designing new business card utilizing our new logo.

BuildMarq Solutions works with Construction Business Owners, Managers & IT Professionals to strengthen software usage and increase user productivity.

Our Construction Accounting and Mobile Field Management Software Clients engage with us in the following areas:

New Software Implementations
Software Re-Implementations
Redesigning Software Usage at the User Level
Project Coordination & Management
Continued Software Support

Old tag line:
Weighing Options - Implementing Solutions

www.buildmarq-solutions.example

Stride 4 is a product, but not needed for a new business card.

```html
<!DOCTYPE html>
<html lang="en">
<head>
<meta charset="utf-8">
<title>BuildMarq Solutions – Business Card</title>
<link rel="stylesheet" href="https://fonts.googleapis.com/css2?family=Open+Sans:wght@400;600;700&family=Arimo:wght@400;700&display=swap">
<style>
  :root {
    --backdrop: #ece6df;
    --kraft-light: #dcb88f;
    --kraft-mid: #cfa67a;
    --kraft-dark: #c0976b;
    --ink: #141210;
    --card-shadow: rgba(40, 25, 10, 0.35);
  }
  * { box-sizing: border-box; margin: 0; padding: 0; }
  html, body {
    width: 1200px;
    height: 900px;
    overflow: hidden;
    background: var(--backdrop);
  }
  .canvas {
    position: relative;
    width: 1200px;
    height: 900px;
  }
  .card {
    position: absolute;
    left: 330px;
    width: 556px;
    height: 343px;
    background: linear-gradient(160deg, var(--kraft-light) 0%, var(--kraft-mid) 50%, var(--kraft-dark) 100%);
    box-shadow: 2px 3px 6px var(--card-shadow);
    color: var(--ink);
    text-align: center;
  }
  .card--front { top: 90px; }
  .card--back { top: 469px; }

  /* Front */
  .contact-name {
    position: absolute;
    top: 62px; left: 0; right: 0;
    font-family: "Open Sans", sans-serif;
    font-weight: 700;
    font-size: 20px;
    letter-spacing: 0.3px;
    line-height: 26px;
  }
  .contact-role {
    position: absolute;
    top: 86px; left: 0; right: 0;
    font-family: "Arimo", sans-serif;
    font-size: 16px;
    line-height: 20px;
  }
  .rule {
    position: absolute;
    left: 180px;
    width: 196px;
    height: 1px;
    background: var(--ink);
  }
  .rule--upper { top: 116px; }
  .rule--lower { top: 222px; }
  .contact-list {
    position: absolute;
    top: 129px; left: 0; right: 0;
    list-style: none;
    font-family: "Arimo", sans-serif;
    font-size: 16px;
    line-height: 20px;
  }
  .contact-list b { font-weight: 700; }
  .contact-address {
    position: absolute;
    top: 239px; left: 0; right: 0;
    font-family: "Arimo", sans-serif;
    font-style: normal;
    font-size: 16px;
    line-height: 20px;
  }

  /* Back */
  .brand {
    position: absolute;
    top: 118px; left: 0; right: 0;
    display: flex;
    justify-content: center;
    align-items: center;
    gap: 18px;
  }
  .brand-mark {
    width: 40px;
    height: 40px;
    background: var(--ink);
  }
  .brand-name {
    font-family: "Open Sans", sans-serif;
    font-weight: 700;
    font-size: 40px;
    letter-spacing: 0.5px;
    line-height: 48px;
  }
  .service-list {
    position: absolute;
    top: 247px; left: 0; right: 0;
    list-style: none;
    font-family: "Open Sans", sans-serif;
    font-size: 15px;
    line-height: 20px;
  }
</style>
</head>
<body>
<main class="canvas">
  <section class="card card--front" aria-label="Business card front">
    <h1 class="contact-name">DANIEL HARTLEY</h1>
    <p class="contact-role">Managing Director</p>
    <div class="rule rule--upper"></div>
    <ul class="contact-list">
      <li><b>P:</b> 044-555 0100 210</li>
      <li><b>M:</b> 044-555 0100 210</li>
      <li><b>E:</b> info@buildmarq-solutions.example</li>
      <li><b>W:</b> www.buildmarq-solutions.example</li>
    </ul>
    <div class="rule rule--lower"></div>
    <address class="contact-address">12345, Address Goes Here<br>Country Name, 123456.</address>
  </section>

  <section class="card card--back" aria-label="Business card back">
    <div class="brand">
      <span class="brand-mark" aria-hidden="true"></span>
      <span class="brand-name">BuildMarq Solutions</span>
    </div>
    <ul class="service-list">
      <li>New Software Implementations | Software Re-Implementations</li>
      <li>Redesigning Software Usage at the User Level</li>
      <li>Project Coordination &amp; Management | Continued Software Support</li>
    </ul>
  </section>
</main>
</body>
</html>
```